THE HEADLAND AT TALL PINE HUDSON RIVER WATERFRONT LAND

crisp clear business cards on wood stock or thick paper with large font with a river otter logo, PERSONAL INFO ON ONE SIDE, PROJECT INFO ON THE OTHER SIDE
Updates

I don’t have a logo. Just thought that a photo of a river otter would look appealing.

Target Market(s)

Buyers and realtors

Industry/Entity Type

Real Estate Development

Contact Information for Business Card

MARTIN KOWALCZYK
607-318-5942 (Call or Text)
STONE MEADOW LLC PRINCIPAL

RQVWFIELD@NORVAMAIL.NET

Font styles to use
Sans Serif

Colors
fbfdfe
0792cd
00a990
fbed22
ec1f27

Requirements
Must have
• LARGE FONT, ROUNDED EDGES,
Nice to have
• ON THE BACK SIDE :
• THE HEADLAND AT TALL PINE
• HUDSON RIVER WATERFRONT LAND
• 2 TO 67 ACRES---READY TO BUILD
• PRICED TO SELL!

```html
<!DOCTYPE html>
<html lang="en">
<head>
<meta charset="utf-8">
<title>The Headland at Tall Pine – Business Card</title>
<link href="https://fonts.googleapis.com/css2?family=Bebas+Neue&family=Cormorant+Garamond:wght@500&family=Quicksand:wght@500&display=swap" rel="stylesheet">
<style>
  :root {
    --backdrop: #e6e6e6;
    --stock: #ece0c4;
    --red: #d3151d;
    --band: #de3f1f;
    --ink: #2a2622;
    --band-text: #fbfdfe;
  }
  * { margin: 0; padding: 0; box-sizing: border-box; }
  html, body { width: 1200px; height: 900px; overflow: hidden; background: var(--backdrop); }
  .canvas { position: relative; width: 1200px; height: 900px; display: flex; flex-direction: column; align-items: center; justify-content: center; gap: 50px; }
  .card {
    position: relative; width: 560px; height: 320px;
    background: var(--stock); border-radius: 34px; overflow: hidden;
    box-shadow: 0 6px 18px rgba(0,0,0,.18);
  }
  .mark {
    position: absolute; border-radius: 50%;
    background: radial-gradient(circle, #d9cba9 0%, #cdbd98 100%);
  }
  /* personal side */
  .person .name {
    position: absolute; left: 46px; top: 40px;
    font-family: "Bebas Neue", sans-serif; font-size: 62px; line-height: 1; color: var(--red); letter-spacing: 1px;
  }
  .person .role {
    position: absolute; left: 48px; top: 104px;
    font-family: "Cormorant Garamond", serif; font-size: 16px; color: var(--ink); letter-spacing: .5px;
  }
  .person .contact { position: absolute; left: 46px; top: 138px; list-style: none; font-family: "Quicksand", sans-serif; color: var(--ink); }
  .person .contact li { display: flex; align-items: center; gap: 8px; font-size: 20px; margin-bottom: 8px; }
  .person .contact small { font-size: 11px; }
  .person .contact svg { width: 14px; height: 14px; fill: var(--ink); }
  .person .mark { right: 50px; bottom: 40px; width: 150px; height: 150px; }
  /* project side */
  .project .mark { right: 110px; top: 28px; width: 80px; height: 80px; }
  .project .title {
    position: absolute; left: 40px; top: 112px;
    font-family: "Bebas Neue", sans-serif; font-size: 60px; line-height: 1; color: var(--red);
  }
  .project .subtitle {
    position: absolute; left: 42px; top: 176px;
    font-family: "Cormorant Garamond", serif; font-size: 23px; color: var(--ink); letter-spacing: 2px;
  }
  .project .band {
    position: absolute; left: 0; right: 0; bottom: 22px; height: 52px; background: var(--band);
    display: flex; align-items: center; padding-left: 42px; gap: 16px;
    font-family: "Bebas Neue", sans-serif; font-size: 24px; color: var(--band-text); letter-spacing: .5px;
  }
</style>
</head>
<body>
<main class="canvas">
  <section class="card project">
    <div class="mark" role="img" aria-label="River otter line illustration"></div>
    <h1 class="title">The Headland at Tall Pine</h1>
    <p class="subtitle">HUDSON RIVER WATERFRONT LAND</p>
    <div class="band"><span>2 to 67 Acres - Ready to Build</span><span>|</span><span>Priced to Sell!</span></div>
  </section>
  <section class="card person">
    <h2 class="name">Martin Kowalczyk</h2>
    <p class="role">STONE MEADOW LLC PRINCIPAL</p>
    <ul class="contact">
      <li><svg viewBox="0 0 24 24" aria-hidden="true"><path d="M6.6 10.8a15 15 0 0 0 6.6 6.6l2.2-2.2a1 1 0 0 1 1-.25 11 11 0 0 0 3.6.6 1 1 0 0 1 1 1V20a1 1 0 0 1-1 1A17 17 0 0 1 3 4a1 1 0 0 1 1-1h3.5a1 1 0 0 1 1 1 11 11 0 0 0 .6 3.6 1 1 0 0 1-.25 1z"/></svg>607-318-5942 <small>(Call or Text)</small></li>
      <li><svg viewBox="0 0 24 24" aria-hidden="true"><path d="M2 5h20v14H2zm2 2v.5l8 5 8-5V7z"/></svg>rqvwfield@norvamail.net</li>
    </ul>
    <div class="mark" role="img" aria-label="River otter line illustration"></div>
  </section>
</main>
</body>
</html>
```